Talvick Industrial Maintenance Business Card

Design a business card with the following information, logo must be included.
Talvick Industrial Maintenance
Dan Pelfrey Jr.
Pone 555-214-7608
email dan.pelfrey.jr@mailvantor.com

```html
<!DOCTYPE html>
<html lang="en">
<head>
<meta charset="utf-8">
<title>Talvick Industrial Maintenance – Business Card</title>
<link rel="stylesheet" href="https://fonts.googleapis.com/css2?family=Montserrat:wght@600;700&family=Roboto:wght@400&display=swap">
<style>
  :root {
    --stage: #e6e6e4;
    --card: #2f2f2f;
    --card-deep: #262626;
    --brand-blue: #0f72c2;
    --text-light: #f2f2f2;
    --divider: #d8d8d8;
    --emboss: #3a3a3a;
  }
  * { margin: 0; padding: 0; box-sizing: border-box; }
  html, body {
    width: 1200px; height: 801px; overflow: hidden;
    background: var(--stage);
  }
  .stage {
    position: relative; width: 1200px; height: 801px;
    display: flex; align-items: center; justify-content: center; gap: 40px;
  }
  .card {
    position: relative; width: 540px; height: 310px;
    background: var(--card); overflow: hidden;
    box-shadow: 0 10px 24px rgba(0,0,0,0.18);
  }
  .card-front::after {
    content: ""; position: absolute; left: 0; right: 0; bottom: 0; height: 7px;
    background: var(--brand-blue);
  }
  .front-brand {
    position: absolute; left: 34px; top: 50%; transform: translateY(-50%);
    display: flex; align-items: center; gap: 10px;
  }
  .brand-dot {
    width: 30px; height: 30px; border-radius: 50%;
    background: var(--brand-blue); flex: none;
  }
  .brand-name {
    font-family: "Montserrat", sans-serif; font-weight: 700;
    color: var(--brand-blue); text-transform: uppercase; line-height: 1.15;
  }
  .front-brand .brand-name { font-size: 14px; width: 170px; }
  .divider {
    position: absolute; left: 262px; top: 100px; width: 1px; height: 110px;
    background: var(--divider);
  }
  .contact {
    position: absolute; left: 284px; top: 50%; transform: translateY(-50%);
  }
  .contact-name {
    font-family: "Montserrat", sans-serif; font-weight: 700; font-size: 19px;
    color: var(--brand-blue); text-transform: uppercase; letter-spacing: 0.5px;
    margin-bottom: 12px;
  }
  .contact-line {
    display: flex; align-items: center; gap: 9px;
    font-family: "Roboto", sans-serif; font-size: 12.5px; color: var(--text-light);
    margin-bottom: 7px;
  }
  .contact-line svg { width: 13px; height: 13px; flex: none; }
  .back-mark {
    position: absolute; left: -40px; top: 40px; width: 290px; height: 290px;
    border-radius: 50%;
    background: radial-gradient(circle at 40% 35%, var(--emboss), var(--card-deep));
  }
  .back-brand {
    position: absolute; right: 30px; bottom: 78px; text-align: left;
  }
  .back-brand .brand-name { font-size: 24px; width: 250px; }
</style>
</head>
<body>
<main class="stage">
  <section class="card card-front" aria-label="Card front">
    <div class="front-brand">
      <span class="brand-dot"></span>
      <span class="brand-name">Talvick Industrial Maintenance</span>
    </div>
    <div class="divider"></div>
    <div class="contact">
      <p class="contact-name">Dan Pelfrey Jr.</p>
      <p class="contact-line">
        <svg viewBox="0 0 24 24" aria-hidden="true"><path fill="#0f72c2" d="M6.6 10.8a15.1 15.1 0 0 0 6.6 6.6l2.2-2.2a1 1 0 0 1 1-.25 11.4 11.4 0 0 0 3.6.57 1 1 0 0 1 1 1V20a1 1 0 0 1-1 1A17 17 0 0 1 3 4a1 1 0 0 1 1-1h3.5a1 1 0 0 1 1 1c0 1.25.2 2.45.57 3.57a1 1 0 0 1-.25 1z"/></svg>
        555-214-7608
      </p>
      <p class="contact-line">
        <svg viewBox="0 0 24 24" aria-hidden="true"><rect x="2.5" y="5" width="19" height="14" rx="1" fill="none" stroke="#0f72c2" stroke-width="2"/><path d="M3 6l9 7 9-7" fill="none" stroke="#0f72c2" stroke-width="2"/></svg>
        dan.pelfrey.jr@mailvantor.com
      </p>
    </div>
  </section>

  <section class="card card-back" aria-label="Card back">
    <div class="back-mark" role="img" aria-label="Large embossed brand emblem"></div>
    <div class="back-brand">
      <span class="brand-name">Talvick Industrial Maintenance</span>
    </div>
  </section>
</main>
</body>
</html>
```